Make it cool to work near where you are...

Calling all creatives - create the ultimate cool card for people who want to cut their commute.

Here at TilloPod we've got what can best be described as an Marlin pass for desks - and we want to brighten up the wallets of our most loyal users.

So, pitch us your ideas and you might see your design on cards being flashed across the country - and we've thrown in a bit of cash too.

Do see our brief card guidelines - with a couple of past examples thrown in.

Industry/Entity Type

Cash

```html
<!DOCTYPE html>
<html lang="en">
<head>
<meta charset="utf-8">
<title>TilloPod Member Card</title>
<link rel="stylesheet" href="https://fonts.googleapis.com/css2?family=Montserrat:wght@700&family=Arimo:wght@400;700&display=swap">
<style>
  :root {
    --backdrop: #ece7e1;
    --brand-pink: #ec1a7e;
    --stripe-pink: #f9cde0;
    --ink: #2d2d2f;
    --number-ink: #111111;
    --white: #ffffff;
    --badge-edge: #d9d9d9;
    --scene-dark: #3a3a3a;
    --scene-green: #8cc251;
    --scene-light: #c7e28f;
  }
  * { box-sizing: border-box; margin: 0; padding: 0; }
  html, body { width: 980px; height: 1200px; overflow: hidden; }
  body {
    background: var(--backdrop);
    position: relative;
    font-family: "Arimo", Arial, sans-serif;
  }
  .card {
    position: absolute;
    left: 78px;
    width: 828px;
    height: 524px;
    background: var(--brand-pink);
    border-radius: 32px;
    overflow: hidden;
  }
  .card--front { top: 41px; }
  .card--back { top: 622px; left: 74px; }

  .brand-pill {
    position: absolute;
    left: 116px;
    top: 49px;
    width: 648px;
    height: 133px;
    background: var(--white);
    border-radius: 67px;
    display: flex;
    align-items: center;
    justify-content: center;
  }
  .brand-name {
    font-family: "Montserrat", Arial, sans-serif;
    font-weight: 700;
    font-size: 78px;
    letter-spacing: -2px;
    color: var(--ink);
  }

  .number-stripe {
    position: absolute;
    left: 0;
    top: 273px;
    width: 100%;
    height: 57px;
    background: var(--stripe-pink);
    display: flex;
    align-items: center;
    padding-left: 75px;
  }
  .card-number {
    font-weight: 700;
    font-size: 36px;
    color: var(--number-ink);
    letter-spacing: 0.5px;
  }

  .city-scene {
    position: absolute;
    left: 0;
    bottom: 0;
    width: 100%;
    height: 92px;
    background: linear-gradient(to bottom,
      var(--scene-dark) 0%, var(--scene-dark) 22%,
      var(--scene-green) 40%, var(--scene-light) 70%, var(--scene-green) 100%);
  }

  .web-address {
    position: absolute;
    left: 246px;
    top: 472px;
    height: 30px;
    padding: 0 12px;
    background: var(--white);
    border-radius: 10px;
    font-size: 22px;
    color: var(--number-ink);
    display: flex;
    align-items: center;
  }

  .mark-badge {
    position: absolute;
    left: 608px;
    top: 377px;
    width: 172px;
    height: 114px;
    background: var(--white);
    border: 3px solid var(--badge-edge);
    border-radius: 22px;
    display: flex;
    align-items: center;
    justify-content: center;
  }
  .mark-initials {
    font-family: "Montserrat", Arial, sans-serif;
    font-weight: 700;
    font-size: 68px;
    color: var(--ink);
  }
</style>
</head>
<body>

  <section class="card card--front">
    <div class="brand-pill"><span class="brand-name">TilloPod</span></div>
    <div class="number-stripe"><span class="card-number">0042 615 370 884</span></div>
    <div class="city-scene" role="img" aria-label="Illustrated city skyline with buildings, towers, trees and rolling green hills"></div>
    <div class="web-address">www.tillopod.com</div>
    <div class="mark-badge"><span class="mark-initials">TP</span></div>
  </section>

  <section class="card card--back">
    <div class="brand-pill"><span class="brand-name">TilloPod</span></div>
    <div class="city-scene" role="img" aria-label="Illustrated city skyline with buildings, towers, trees and rolling green hills"></div>
    <div class="web-address">www.tillopod.com</div>
    <div class="mark-badge"><span class="mark-initials">TP</span></div>
  </section>

</body>
</html>
```